Commercial Bakery needs packing design for a Bread Bag.

Dorne's Bakery needs a design for a bread bag to be distributed to grocery stores. We make all kinds of breads and want this packaging to represent our company. We would like the packaging to be black and white with a fun/bubbly modern design. I have attached a few ideas of what I am looking for.
There are 5 different products. Packaging must be the same for each product except for corresponding product name, bar code and nutrional facts.
Product names:
Coconut Cream Bread
Cream Bread
Potato Rolls
Roll ups
Coconut & Raisin Bread

Our products are packaged in a 11” x 8” poly bag.
I will open 5 contracts with whoever’s design I select. I will then provide nutritional facts, barcodes for items once a contract is selected. Thank you!!

Target Market(s)

Grocery stores

Industry/Entity Type

Bakery

Requirements
Must have
• Black and White (off whites are ok)
Should not have
• Color

```html
<!DOCTYPE html>
<html lang="en">
<head>
<meta charset="utf-8">
<title>Dorne's Bakery – Coconut Cream Bread Bag</title>
<link rel="stylesheet" href="https://fonts.googleapis.com/css2?family=Lato:wght@400;700;900&display=swap">
<style>
  :root {
    --backdrop: #9a9a9a;
    --ink: #111111;
    --paper: #ffffff;
    --film: #f1f1f1;
    --crust-light: #d7a56e;
    --crust-dark: #b98250;
  }
  html, body {
    margin: 0;
    padding: 0;
    width: 800px;
    height: 1200px;
    overflow: hidden;
    background: var(--backdrop);
  }
  .bag-artwork {
    display: block;
    width: 800px;
    height: 1200px;
    font-family: "Lato", Arial, sans-serif;
  }
  .brand-name { font-weight: 900; font-size: 26px; fill: var(--ink); }
  .product-name { font-weight: 700; font-size: 37px; fill: var(--ink); letter-spacing: 0.5px; }
  .product-type { font-weight: 700; font-size: 34px; fill: var(--paper); letter-spacing: 1px; }
  .net-weight { font-weight: 700; font-size: 12.5px; fill: var(--ink); }
</style>
</head>
<body>
<svg class="bag-artwork" viewBox="0 0 800 1200" xmlns="http://www.w3.org/2000/svg">
  <defs>
    <linearGradient id="loafTone" x1="0" y1="0" x2="1" y2="0">
      <stop offset="0" stop-color="var(--crust-dark)"/>
      <stop offset="0.5" stop-color="var(--crust-light)"/>
      <stop offset="1" stop-color="var(--crust-dark)"/>
    </linearGradient>
    <pattern id="scallopTop" patternUnits="userSpaceOnUse" x="235" y="634" width="12" height="12">
      <circle cx="6" cy="6" r="6" fill="var(--paper)"/>
    </pattern>
    <pattern id="scallopBottom" patternUnits="userSpaceOnUse" x="235" y="946" width="12" height="12">
      <circle cx="6" cy="6" r="6" fill="var(--paper)"/>
    </pattern>
  </defs>

  <!-- gathered bag top -->
  <path class="bag-top" role="img" aria-label="Printed bag top with repeating wheat stalk and brand pattern"
        d="M393 378 L196 172 Q400 62 606 176 L418 378 Z" fill="var(--film)"/>
  <ellipse class="bag-tie" cx="406" cy="379" rx="10" ry="5" fill="var(--ink)"/>

  <!-- bag body with visible loaf -->
  <rect class="loaf-window" role="img" aria-label="Sliced bread loaf visible through the clear bag"
        x="235" y="388" width="347" height="658" rx="16" fill="url(#loafTone)"/>

  <!-- label band -->
  <g class="label-band">
    <rect x="235" y="640" width="347" height="312" fill="var(--paper)"/>
    <rect x="235" y="634" width="347" height="6" fill="url(#scallopTop)"/>
    <rect x="235" y="952" width="347" height="6" fill="url(#scallopBottom)"/>
  </g>

  <!-- brand -->
  <g class="brand">
    <circle cx="408" cy="672" r="24" fill="var(--ink)"/>
    <text class="brand-name" x="408" y="738" text-anchor="middle">Dorne's Bakery</text>
  </g>

  <!-- product title -->
  <g class="product-title">
    <text class="product-name" x="408" y="818" text-anchor="middle">COCONUT CREAM</text>
    <g class="rule-left" stroke="var(--ink)">
      <line x1="258" y1="847" x2="328" y2="847" stroke-width="1.5"/>
      <line x1="290" y1="852" x2="328" y2="852" stroke-width="1.5"/>
    </g>
    <rect x="334" y="830" width="148" height="40" rx="5" fill="var(--ink)"/>
    <text class="product-type" x="408" y="863" text-anchor="middle">BREAD</text>
    <g class="rule-right" stroke="var(--ink)">
      <line x1="488" y1="847" x2="558" y2="847" stroke-width="1.5"/>
      <line x1="488" y1="852" x2="526" y2="852" stroke-width="1.5"/>
    </g>
  </g>

  <text class="net-weight" x="408" y="924" text-anchor="middle">NET WT 18 OZ (510g)</text>
</svg>
</body>
</html>
```